New Business Card for Software Company

We are looking at rebranding a 10 year old company that specializes in PDF and DWF solutions for Architects and Engineers. We will attach the new company logo that we are going with so you can work with that and complimentary colors.
The sample information we would like on the business card is:
Gerald Pinsworth
Vice President
4817 W. Larkspur Avenue. STE 306
PMB#514
Mesa, AZ 85371
877-392-5140 US Toll Free
123-456-2914 Cell
gpinsworth@vexolitra.com
The old tag line that we had on the business cars was.
Delivering Dependable Drawing Conversion Tools for Architects and Engineers Everywhere.
If you have an idea for a better tag line we are open to that also.
Updates
We would like to thank all of the Designers for their wonderful work. We apologize that we will not have the time to provide feedback to everyone. There is just so many innovative and professional designs that you have all created making our decision even harder.
Target Market(s)
Architects and Engineers
Industry/Entity Type
Business
Look and feel
Each slider illustrates characteristics of the customer's brand and the style your logo design should communicate.

```html
<!DOCTYPE html>
<html lang="en">
<head>
<meta charset="utf-8">
<title>Vexolitra Business Card</title>
<link href="https://fonts.googleapis.com/css2?family=PT+Sans:ital,wght@0,700;1,700&display=swap" rel="stylesheet">
<style>
  :root {
    --orange-deep: #ee5a2a;
    --orange-mid: #f47b2a;
    --orange-light: #f8a33a;
    --grey: #6b6b6b;
    --ink: #1a1a1a;
    --white: #ffffff;
    --green-edge: #d3e8b5;
    --green-mid: #8fc74a;
  }
  * { margin: 0; padding: 0; box-sizing: border-box; }
  html, body { width: 1200px; height: 914px; overflow: hidden; }
  body {
    position: relative;
    background: linear-gradient(90deg, var(--green-edge) 0%, var(--green-mid) 50%, var(--green-edge) 100%);
    font-family: "PT Sans", "Helvetica Neue", Arial, sans-serif;
    color: var(--ink);
  }
  .card { position: absolute; width: 662px; height: 378px; overflow: hidden; background: var(--white); }
  .card svg.art { position: absolute; inset: 0; }
  .card--front { left: 73px; top: 62px; }
  .card--back { left: 474px; top: 482px; }

  .brand { position: absolute; display: flex; align-items: center; gap: 14px; }
  .brand__dot { border-radius: 50%; background: var(--orange-deep); }
  .brand__name { font-weight: 700; color: var(--orange-deep); line-height: 1; letter-spacing: -0.5px; }

  .card--front .brand { left: 140px; top: 100px; }
  .card--front .brand__dot { width: 86px; height: 86px; }
  .card--front .brand__name { font-size: 76px; }

  .tagline { position: absolute; font-style: italic; font-weight: 700; font-size: 16px; white-space: nowrap; }
  .tagline--one { left: 34px; top: 260px; }
  .tagline--two { left: 149px; top: 284px; }

  .card--back .brand { left: 128px; top: 10px; }
  .card--back .brand__dot { width: 68px; height: 68px; }
  .card--back .brand__name { font-size: 56px; }

  .person { position: absolute; left: 211px; top: 114px; font-style: italic; font-weight: 700; font-size: 22px; line-height: 29px; }
  .contact { position: absolute; left: 211px; top: 207px; font-weight: 700; font-size: 17px; line-height: 23.8px; font-style: normal; }
</style>
</head>
<body>

<section class="card card--front">
  <svg class="art" width="662" height="378" viewBox="0 0 662 378" aria-hidden="true">
    <defs>
      <linearGradient id="frontOrange" x1="0" x2="1" y1="0" y2="0">
        <stop offset="0" stop-color="#ee5a2a"/>
        <stop offset="0.5" stop-color="#f8a33a"/>
        <stop offset="1" stop-color="#ee5a2a"/>
      </linearGradient>
    </defs>
    <rect width="662" height="378" fill="url(#frontOrange)"/>
    <path d="M215 0 Q20 110 0 362 L0 378 L440 378 C600 330 660 170 662 0 Z" fill="var(--grey)"/>
    <path d="M245 0 Q40 130 2 378 L420 378 C580 330 640 160 650 0 Z" fill="var(--white)"/>
  </svg>
  <div class="brand">
    <span class="brand__dot"></span>
    <span class="brand__name">Vexolitra</span>
  </div>
  <p class="tagline tagline--one">Delivering Dependable Drawing Conversion</p>
  <p class="tagline tagline--two">Tools for Architects and Engineers Everywhere .........</p>
</section>

<section class="card card--back">
  <svg class="art" width="662" height="378" viewBox="0 0 662 378" aria-hidden="true">
    <defs>
      <linearGradient id="stripeFade" x1="0" x2="1" y1="0" y2="0">
        <stop offset="0" stop-color="#ee5a2a"/>
        <stop offset="0.14" stop-color="#f8a33a"/>
        <stop offset="0.3" stop-color="#ffffff"/>
        <stop offset="0.7" stop-color="#ffffff"/>
        <stop offset="0.86" stop-color="#f8a33a"/>
        <stop offset="1" stop-color="#ee5a2a"/>
      </linearGradient>
    </defs>
    <g class="stripes" fill="url(#stripeFade)">
      <rect x="0" y="100" width="662" height="22"/>
      <rect x="0" y="129" width="662" height="22"/>
      <rect x="0" y="158" width="662" height="22"/>
      <rect x="0" y="187" width="662" height="22"/>
      <rect x="0" y="216" width="662" height="22"/>
      <rect x="0" y="245" width="662" height="22"/>
      <rect x="0" y="274" width="662" height="22"/>
      <rect x="0" y="303" width="662" height="22"/>
      <rect x="0" y="332" width="662" height="22"/>
    </g>
    <ellipse cx="331" cy="236" rx="212" ry="220" fill="var(--white)"/>
  </svg>
  <div class="brand">
    <span class="brand__dot"></span>
    <span class="brand__name">Vexolitra</span>
  </div>
  <p class="person">Gerald Pinsworth<br>Vice President</p>
  <address class="contact">
    4817 W. Larkspur Avenue. STE 306<br>
    PMB#514<br>
    Mesa, AZ 85371<br>
    877-392-5140 US Toll Free<br>
    123-456-2914 Cell<br>
    gpinsworth@vexolitra.com
  </address>
</section>

</body>
</html>
```